Veterinary Hospital Brochure - 2 Drafts - 1 Normal and 1 Fun.

Meadowbrook Pet Hospital needs a brochure to promote our veterinary hospital. These will be delivered to local mailboxes. I would like to see atleast 2 submissions from each designer.
One submission conservative and A4 folded DL and another submission more radical and interesting with innovative folding or crazy concepts. Maybe the brochure could be designed to fold into a dog house ?
I want at least one version to be VERY SIMPLE AND INTIMATE.
Our existing website is here: http://furlane.example/ and our new website will look like this: http://trial4.pagemint.example/#home
Please use colors and images from the new website, and information from the old website. The heading font used in the new site is Qorvatype - Otter Tilt Sketchline
I want the brochure to be simple and engaging on first view, and then provide the opportunity to find more information if desired. The brochure needs to be captivating on the outside so people don't throw it away immediately.

We will soon need letterhead, flags, pens, business cards, signs and vouchers so there is the opportunity for more work for the successful designer.

Target Market(s)

Women 25 to 44

Industry/Entity Type

Veterinary

Contact Information for Business Card

Meadowbrook Pet Hospital
14 Marlow Crescent
Tamsworth Vale
NSW 2417
Phone: 02 61938205
Emergency: 0417360592
Fax: 02 83159462
www.meadowbrookvets.example
contact@meadowbrookvets.example

Font styles to use
Script

Requirements
Must have
• Colors from the new website: http://meadowbrookvets.example/ and new logo.
• Information from the old website: http://furlane.example/
• 2 drafts - A normal A4 folded DL flyer and an interesting crazy design.
Nice to have
• VERY SIMPLE
• Subdued
• Intimate
Should not have
• Intense colours
• Red

```html
<!DOCTYPE html>
<html lang="en">
<head>
<meta charset="utf-8">
<title>Meadowbrook Pet Hospital – Brochure</title>
<link rel="stylesheet" href="https://fonts.googleapis.com/css2?family=Sacramento&family=Montserrat:wght@500;600&family=Gochi+Hand&display=swap">
<style>
  :root {
    --wood: #ead8a6;
    --ink: #4b3522;
    --bubble: #ffffff;
    --bubble-line: #3a2a1a;
    --page: #ffffff;
  }
  * { margin: 0; padding: 0; box-sizing: border-box; }
  html, body { width: 1200px; height: 927px; overflow: hidden; background: var(--page); }
  .brochure { position: relative; width: 1200px; height: 927px; overflow: hidden; }
  .house-shape { position: absolute; left: 0; top: 0; }
  .panel { position: absolute; top: 0; width: 400px; height: 705px; color: var(--ink); }
  .panel--left { left: 0; }
  .panel--middle { left: 400px; }
  .panel--right { left: 800px; }
  .heading {
    position: absolute;
    left: 0;
    width: 400px;
    font-family: "Sacramento", cursive;
    font-weight: 400;
    font-size: 52px;
    line-height: 46px;
    text-align: center;
    white-space: nowrap;
    color: var(--ink);
    -webkit-text-stroke: 0.5px var(--ink);
  }
  .body-text {
    position: absolute;
    left: 55px;
    width: 292px;
    font-family: "Montserrat", sans-serif;
    font-weight: 500;
    font-size: 16px;
    line-height: 21.8px;
    text-align: justify;
    letter-spacing: 0.1px;
    hyphens: auto;
    -webkit-hyphens: auto;
  }
  .heading-surgery { top: 228px; }
  .text-surgery { top: 339px; }
  .heading-puppy { top: 466px; font-size: 56px; }
  .text-puppy { top: 527px; }
  .heading-history { top: 236px; font-size: 56px; }
  .text-history { top: 302px; hyphens: manual; -webkit-hyphens: manual; }
  .web-link { font-weight: 600; font-size: 18px; text-align: left; display: block; margin-top: 2px; }
  .heading-services { top: 236px; font-size: 56px; }
  .service-list {
    position: absolute; left: 53px; top: 303px; list-style: none;
    font-family: "Montserrat", sans-serif; font-weight: 500; font-size: 16.5px; line-height: 24.3px;
  }
  .service-list li { display: flex; align-items: center; gap: 5px; }
  .paw { width: 13px; height: 13px; flex: none; }
  .photo { position: absolute; top: 705px; height: 222px; width: 400px; }
  .photo--dog-run { left: 0; background: linear-gradient(180deg, #2f3a22 0%, #4f6b2e 35%, #6f8e3a 70%, #5a7a30 100%); }
  .photo--cat { left: 400px; background: radial-gradient(ellipse at 45% 60%, #c98a4a 0%, #8a6a52 40%, #4a5a6a 100%); }
  .photo--vet-visit { left: 800px; background: linear-gradient(90deg, #d9d8d2 0%, #bfb6a8 40%, #a07a52 70%, #e4e2dc 100%); }
  .bubble { position: absolute; }
  .bubble-text {
    position: absolute; font-family: "Gochi Hand", cursive; color: var(--bubble-line);
    text-align: center; line-height: 0.95;
  }
  .bubble--exercise { left: 130px; top: 696px; width: 200px; height: 120px; }
  .bubble--exercise .bubble-text { left: 26px; top: 20px; width: 170px; font-size: 27px; transform: rotate(-10deg); }
  .bubble--thanks { left: 630px; top: 656px; width: 180px; height: 100px; }
  .bubble--thanks .bubble-text { left: 20px; top: 22px; width: 150px; font-size: 23px; transform: rotate(-10deg); }
</style>
</head>
<body>
<main class="brochure">
  <svg class="house-shape" width="1200" height="927" viewBox="0 0 1200 927" aria-hidden="true">
    <polygon points="0,255 200,0 400,255 600,0 800,255 1000,0 1200,255 1200,705 0,705" fill="var(--wood)"/>
  </svg>

  <section class="panel panel--left">
    <h2 class="heading heading-surgery">Companion<br>Animal Surgery</h2>
    <p class="body-text text-surgery">Meadowbrook Pet Hospital has the latest surgical instrumentation and anaesthetic monitoring to ensure the success of surgery and outcomes for your pets.</p>
    <h2 class="heading heading-puppy">Puppy School</h2>
    <p class="body-text text-puppy">Puppy Pre-School is an essential first step for all puppies regardless of breed or owner education.<br>The classes are so much fun. You will learn heaps and your puppy will have a great time socialising.</p>
  </section>

  <section class="panel panel--middle">
    <h2 class="heading heading-history">History</h2>
    <p class="body-text text-history">Meadowbrook Pet Hospital is built on the grounds of a chapel built in 1897. The chapel hall has been converted into a beautiful reception area.<br>We have constructed a modern veterinary hospital with small animal surgical facilities, X-ray, ultrasound, dog and cat wards, laboratory, isolation, multiple consultation rooms and a huge treatment area.<br>Come in for a tour of our facility or go online:<span class="web-link">www.furlane.example</span></p>
  </section>

  <section class="panel panel--right">
    <h2 class="heading heading-services">Services</h2>
    <ul class="service-list">
      <li><svg class="paw" viewBox="0 0 12 12"><g fill="var(--ink)"><ellipse cx="6" cy="8.3" rx="3" ry="2.5"/><circle cx="2" cy="5" r="1.3"/><circle cx="4.5" cy="2.3" r="1.3"/><circle cx="7.5" cy="2.3" r="1.3"/><circle cx="10" cy="5" r="1.3"/></g></svg>Vaccinations</li>
      <li><svg class="paw" viewBox="0 0 12 12"><g fill="var(--ink)"><ellipse cx="6" cy="8.3" rx="3" ry="2.5"/><circle cx="2" cy="5" r="1.3"/><circle cx="4.5" cy="2.3" r="1.3"/><circle cx="7.5" cy="2.3" r="1.3"/><circle cx="10" cy="5" r="1.3"/></g></svg>Companion Animal De-sexing</li>
      <li><svg class="paw" viewBox="0 0 12 12"><g fill="var(--ink)"><ellipse cx="6" cy="8.3" rx="3" ry="2.5"/><circle cx="2" cy="5" r="1.3"/><circle cx="4.5" cy="2.3" r="1.3"/><circle cx="7.5" cy="2.3" r="1.3"/><circle cx="10" cy="5" r="1.3"/></g></svg>Emergency Surgery</li>
      <li><svg class="paw" viewBox="0 0 12 12"><g fill="var(--ink)"><ellipse cx="6" cy="8.3" rx="3" ry="2.5"/><circle cx="2" cy="5" r="1.3"/><circle cx="4.5" cy="2.3" r="1.3"/><circle cx="7.5" cy="2.3" r="1.3"/><circle cx="10" cy="5" r="1.3"/></g></svg>Dental</li>
      <li><svg class="paw" viewBox="0 0 12 12"><g fill="var(--ink)"><ellipse cx="6" cy="8.3" rx="3" ry="2.5"/><circle cx="2" cy="5" r="1.3"/><circle cx="4.5" cy="2.3" r="1.3"/><circle cx="7.5" cy="2.3" r="1.3"/><circle cx="10" cy="5" r="1.3"/></g></svg>Caeserian</li>
      <li><svg class="paw" viewBox="0 0 12 12"><g fill="var(--ink)"><ellipse cx="6" cy="8.3" rx="3" ry="2.5"/><circle cx="2" cy="5" r="1.3"/><circle cx="4.5" cy="2.3" r="1.3"/><circle cx="7.5" cy="2.3" r="1.3"/><circle cx="10" cy="5" r="1.3"/></g></svg>Behaviour Consults</li>
      <li><svg class="paw" viewBox="0 0 12 12"><g fill="var(--ink)"><ellipse cx="6" cy="8.3" rx="3" ry="2.5"/><circle cx="2" cy="5" r="1.3"/><circle cx="4.5" cy="2.3" r="1.3"/><circle cx="7.5" cy="2.3" r="1.3"/><circle cx="10" cy="5" r="1.3"/></g></svg>Aged Care Consults</li>
      <li><svg class="paw" viewBox="0 0 12 12"><g fill="var(--ink)"><ellipse cx="6" cy="8.3" rx="3" ry="2.5"/><circle cx="2" cy="5" r="1.3"/><circle cx="4.5" cy="2.3" r="1.3"/><circle cx="7.5" cy="2.3" r="1.3"/><circle cx="10" cy="5" r="1.3"/></g></svg>Nutrition Advice</li>
      <li><svg class="paw" viewBox="0 0 12 12"><g fill="var(--ink)"><ellipse cx="6" cy="8.3" rx="3" ry="2.5"/><circle cx="2" cy="5" r="1.3"/><circle cx="4.5" cy="2.3" r="1.3"/><circle cx="7.5" cy="2.3" r="1.3"/><circle cx="10" cy="5" r="1.3"/></g></svg>Flea Treatments</li>
      <li><svg class="paw" viewBox="0 0 12 12"><g fill="var(--ink)"><ellipse cx="6" cy="8.3" rx="3" ry="2.5"/><circle cx="2" cy="5" r="1.3"/><circle cx="4.5" cy="2.3" r="1.3"/><circle cx="7.5" cy="2.3" r="1.3"/><circle cx="10" cy="5" r="1.3"/></g></svg>Radiology</li>
      <li><svg class="paw" viewBox="0 0 12 12"><g fill="var(--ink)"><ellipse cx="6" cy="8.3" rx="3" ry="2.5"/><circle cx="2" cy="5" r="1.3"/><circle cx="4.5" cy="2.3" r="1.3"/><circle cx="7.5" cy="2.3" r="1.3"/><circle cx="10" cy="5" r="1.3"/></g></svg>Ultrasound</li>
      <li><svg class="paw" viewBox="0 0 12 12"><g fill="var(--ink)"><ellipse cx="6" cy="8.3" rx="3" ry="2.5"/><circle cx="2" cy="5" r="1.3"/><circle cx="4.5" cy="2.3" r="1.3"/><circle cx="7.5" cy="2.3" r="1.3"/><circle cx="10" cy="5" r="1.3"/></g></svg>Routine Blood Tests</li>
      <li><svg class="paw" viewBox="0 0 12 12"><g fill="var(--ink)"><ellipse cx="6" cy="8.3" rx="3" ry="2.5"/><circle cx="2" cy="5" r="1.3"/><circle cx="4.5" cy="2.3" r="1.3"/><circle cx="7.5" cy="2.3" r="1.3"/><circle cx="10" cy="5" r="1.3"/></g></svg>Orthopaedic Surgery</li>
      <li><svg class="paw" viewBox="0 0 12 12"><g fill="var(--ink)"><ellipse cx="6" cy="8.3" rx="3" ry="2.5"/><circle cx="2" cy="5" r="1.3"/><circle cx="4.5" cy="2.3" r="1.3"/><circle cx="7.5" cy="2.3" r="1.3"/><circle cx="10" cy="5" r="1.3"/></g></svg>Cruiciate Repair</li>
      <li><svg class="paw" viewBox="0 0 12 12"><g fill="var(--ink)"><ellipse cx="6" cy="8.3" rx="3" ry="2.5"/><circle cx="2" cy="5" r="1.3"/><circle cx="4.5" cy="2.3" r="1.3"/><circle cx="7.5" cy="2.3" r="1.3"/><circle cx="10" cy="5" r="1.3"/></g></svg>Grieving Support</li>
      <li><svg class="paw" viewBox="0 0 12 12"><g fill="var(--ink)"><ellipse cx="6" cy="8.3" rx="3" ry="2.5"/><circle cx="2" cy="5" r="1.3"/><circle cx="4.5" cy="2.3" r="1.3"/><circle cx="7.5" cy="2.3" r="1.3"/><circle cx="10" cy="5" r="1.3"/></g></svg>Skin Treatments</li>
    </ul>
  </section>

  <div class="photo photo--dog-run" role="img" aria-label="Photo of a dog running across a grassy field carrying a toy"></div>
  <div class="photo photo--cat" role="img" aria-label="Photo of a ginger cat lying on the floor"></div>
  <div class="photo photo--vet-visit" role="img" aria-label="Photo of two vet staff members caring for a dog"></div>

  <div class="bubble bubble--exercise">
    <svg width="200" height="120" viewBox="0 0 200 120" aria-hidden="true">
      <path d="M100,6 C152,4 194,22 192,50 C190,80 150,94 100,92 C82,92 66,89 54,84 L28,110 L40,78 C20,70 8,58 10,46 C14,22 52,8 100,6 Z" fill="var(--bubble)" stroke="var(--bubble-line)" stroke-width="2"/>
    </svg>
    <div class="bubble-text">Keep Calm<br>and Exercise</div>
  </div>

  <div class="bubble bubble--thanks">
    <svg width="180" height="100" viewBox="0 0 180 100" aria-hidden="true">
      <path d="M92,4 C140,3 176,18 174,42 C172,66 138,78 94,77 C80,77 66,75 56,71 L18,92 L38,64 C20,58 8,48 10,38 C14,18 48,5 92,4 Z" fill="var(--bubble)" stroke="var(--bubble-line)" stroke-width="2"/>
    </svg>
    <div class="bubble-text">Thanks<br>for visiting</div>
  </div>
</main>
</body>
</html>
```